Refinement of Website & Hubspot Integration

We are launching a new business and require Wordpress and Hubspot support. Unfortunately the designer that we assigned to the task let us down and did not complete the project. This is now time sensitive as we have lost weeks of working time. We require general refinement of the existing website and assistance with photos, menus etc. We also need to build a few simple customer forms. The website also needs to be FULLY mobile optimised. We have also been recommended to sign up for Hubspot (which I have done) as we will be using this for all our mailing campaigns. The designer will need to set this up for us and assist with email templates and some general assistance with helping us use Hubspot. We are looking to develop a long term partnership with a designer that can work alongside us as we grow www.quillmarsh.com.au

Coding

```html
<!DOCTYPE html>
<html lang="en">
<head>
<meta charset="utf-8">
<title>Quillmarsh – We're in the Business of Business</title>
<link href="https://fonts.googleapis.com/css2?family=Marcellus&family=Lato:ital,wght@0,300;0,400;0,700;1,400&display=swap" rel="stylesheet">
<style>
:root{
  --rose:#b07674;
  --rose-deep:#9c6361;
  --ink:#1f1f1f;
  --text:#4a4a4a;
  --muted:#8a8a8a;
  --paper:#ffffff;
  --mist:#f1f0f0;
  --line:#c9a4a3;
  --night:#2e2e30;
}
*{margin:0;padding:0;box-sizing:border-box}
html,body{width:1200px;height:4107px;overflow:hidden}
body{position:relative;background:var(--paper);font-family:'Lato',sans-serif;color:var(--text)}
.abs{position:absolute}
.display{font-family:'Marcellus',serif;font-weight:400;text-transform:uppercase;letter-spacing:.5px}
.btn{position:absolute;display:flex;align-items:center;justify-content:center;font-family:'Lato',sans-serif;font-size:11px;letter-spacing:.5px;text-transform:uppercase}
.btn-dark{background:var(--ink);color:#fff;box-shadow:3px 3px 0 var(--rose)}
.btn-rose{background:var(--rose);color:#fff;box-shadow:3px 3px 0 #fff}
.btn-light{background:#fff;color:var(--ink);box-shadow:3px 3px 0 var(--rose)}
.photo{position:absolute}

/* header */
.site-header{position:absolute;left:0;top:0;width:1200px;height:84px;background:#fff}
.brand{position:absolute;font-family:'Marcellus',serif;color:var(--rose);font-size:33px;letter-spacing:1px;text-transform:uppercase}
.nav a{position:absolute;top:34px;font-size:12px;color:var(--ink);text-decoration:none;letter-spacing:.3px}
.nav a.active{color:var(--rose)}
.nav a.active::after{content:"";position:absolute;left:0;right:0;top:-34px;height:0}

/* hero */
.hero{position:absolute;left:0;top:84px;width:1200px;height:549px}
.hero-title{position:absolute;left:148px;top:340px;font-size:41px;line-height:46px;color:#fff}
.hero-title span{color:var(--rose)}
.hero-copy{position:absolute;left:148px;top:450px;width:460px;font-size:16px;line-height:24px;color:#f2f2f2}

/* about */
.section-heading{font-size:31px;color:var(--ink);line-height:38px}
.body-copy{font-size:14.5px;line-height:22.5px;text-align:justify;color:var(--text)}

/* services */
.card-title{position:absolute;width:100%;text-align:center;font-size:25px}
.card-copy{position:absolute;left:20px;right:20px;font-size:14px;line-height:22.5px;text-align:justify;text-align-last:center}
.round{position:absolute;width:34px;height:34px;border-radius:50%;display:flex;align-items:center;justify-content:center}

/* testimonial */
.quote-card{position:absolute;width:442px;height:224px;background:var(--mist)}
.quote-mark{position:absolute;left:32px;top:-22px;width:59px;height:57px;border-top:2px solid var(--rose);border-right:2px solid var(--rose);background:var(--mist);display:flex;align-items:center;justify-content:center}
.quote-text{position:absolute;left:22px;right:22px;top:60px;font-size:13px;font-style:italic;line-height:22.5px;color:var(--text)}

/* form */
.field{position:absolute;border:1px solid #c9c2c2;background:#fff;font-size:12px;color:#555;padding:10px 16px}

/* footer */
.site-footer{position:absolute;left:0;top:3768px;width:1200px;height:339px;background:var(--rose)}
.footer-head{position:absolute;font-family:'Marcellus',serif;color:#fff;font-size:17px;text-transform:uppercase}
.footer-link{position:absolute;font-size:11px;color:#fff;text-transform:uppercase;letter-spacing:.3px}
.social{position:absolute;width:34px;height:34px;background:#fff;box-shadow:3px 3px 0 var(--ink)}
.radio{position:absolute;font-size:10.5px;color:#fff;display:flex;align-items:center;gap:8px}
.radio i{width:13px;height:13px;border:1px solid #fff;border-radius:50%;display:inline-block;position:relative}
.radio i.on::after{content:"";position:absolute;left:3px;top:3px;width:5px;height:5px;border-radius:50%;background:#fff}
</style>
</head>
<body>

<header class="site-header">
  <div class="brand" style="left:148px;top:32px">Quillmarsh</div>
  <nav class="nav">
    <a class="active" style="left:537px">HOME</a>
    <a style="left:606px">ABOUT US</a>
    <a style="left:698px">OUR SERVICES ⌄</a>
    <a style="left:834px">APPROACH</a>
  </nav>
  <div class="btn btn-rose" style="left:939px;top:26px;width:115px;height:33px;box-shadow:3px 3px 0 var(--ink)">Contact Us</div>
</header>

<section class="hero">
  <div class="photo" role="img" aria-label="Business team of four colleagues talking in a bright modern office" style="left:0;top:0;width:1200px;height:549px;background:linear-gradient(100deg,#2b2a2a 0%,#4a4540 40%,#3a3a3c 70%,#262628 100%)"></div>
</section>
<h1 class="display hero-title">
  <span>Quillmarsh -</span><br>We're in the business of business
</h1>
<p class="hero-copy">We are experts at inspiring audiences to engage and make decisive decisions with strong offers..</p>
<div class="btn btn-rose" style="left:148px;top:513px;width:171px;height:35px">Consultation Now!</div>

<!-- about -->
<div class="abs" style="left:154px;top:712px;width:415px;height:469px;background:var(--ink)"></div>
<div class="photo" role="img" aria-label="Two colleagues reviewing work on a tablet at a desk" style="left:148px;top:706px;width:413px;height:469px;background:linear-gradient(160deg,#d9d6d2 0%,#b7b1ab 50%,#7b746e 100%)"></div>
<h2 class="display section-heading abs" style="left:610px;top:748px">About the<br><span style="color:var(--rose);font-size:37px">Quillmarsh</span></h2>
<p class="body-copy abs" style="left:610px;top:842px;width:444px">Welcome to <b style="color:var(--ink)">Quillmarsh</b>, where we are challenging the traditional format of business sales in Canberra and surrounding regions, bringing a long overdue fresh approach to the market. Quillmarsh is not your typical business brokerage firm; we are a team of seasoned professionals who have mastered the art of successful company operation and thrived in the local SME space for over two decades...</p>
<p class="body-copy abs" style="left:610px;top:1022px;width:444px">Our expertise and experience extends beyond the ability to represent a company during a sales transaction.</p>
<div class="btn btn-dark" style="left:610px;top:1090px;width:133px;height:35px">Explore Now!</div>

<!-- approach -->
<div class="photo" role="img" aria-label="Faded photo of a business meeting around a table" style="left:0;top:1253px;width:1200px;height:365px;background:linear-gradient(90deg,#f6f6f6 0%,#ececec 45%,#d9d9d9 100%)"></div>
<h2 class="display section-heading abs" style="left:0;width:1200px;text-align:center;top:1316px;font-size:36px">My Approach</h2>
<p class="abs" style="left:212px;top:1376px;width:776px;font-size:14.5px;line-height:22.5px;text-align:justify;text-align-last:center;color:#444">Irrespective of your operation's scale or revenue, we embark on a crucial, in-depth exploration to fully understand your service offering, competitive advantage and position in the market. It is our job to learn and optimise your position in order to secure a top-tier proposal. Offering a fresh perspective, we meticulously assess every facet, adopting the vantage point of prospective buyers. This ensures your business is primed and positioned to captivate and maximise qualified contenders, eager to present premium offers.</p>
<div class="btn btn-dark" style="left:534px;top:1514px;width:131px;height:34px">Explore Now!</div>

<!-- services -->
<h2 class="display section-heading abs" style="left:0;width:1200px;text-align:center;top:1682px;font-size:36px">Our Services</h2>

<div class="abs" style="left:220px;top:1752px;width:370px;height:586px;background:var(--rose)"></div>
<div class="abs" style="left:212px;top:1744px;width:370px;height:586px;background:var(--mist)">
  <div class="photo" role="img" aria-label="Handshake over a laptop with cash being passed" style="left:0;top:0;width:370px;height:371px;background:linear-gradient(150deg,#6e6a66 0%,#2c2b2a 60%,#8b7a62 100%)"></div>
  <div class="display card-title" style="top:388px;color:var(--ink)">Buying a Business</div>
  <p class="card-copy" style="top:430px">Whether you're a first-time business buyer or a seasoned entrepreneur with a successful track record, we understand that the journey from initial consideration to sealing the deal can be a daunting one.</p>
  <div class="abs" style="left:8px;top:580px;width:362px;height:6px;background:var(--rose)"></div>
  <div class="round" style="left:168px;top:569px;background:#fff">
    <svg width="12" height="10" viewBox="0 0 12 10"><path d="M1 5h10M7 1l4 4-4 4" stroke="#1f1f1f" stroke-width="1.2" fill="none"/></svg>
  </div>
</div>

<div class="abs" style="left:618px;top:1744px;width:370px;height:586px;background:var(--rose)">
  <div class="photo" role="img" aria-label="Three people smiling and shaking hands across a meeting table" style="left:0;top:0;width:370px;height:371px;background:linear-gradient(150deg,#9aa89a 0%,#cfcfcb 45%,#55575b 100%)"></div>
  <div class="display card-title" style="top:388px;color:#fff">Selling My Business</div>
  <p class="card-copy" style="top:430px;color:#fff">Welcome to Quillmarsh – your premier choice for business brokerage services from Canberra to the Coast. What sets us apart is an unparalleled ability to navigate diverse industry landscapes, seamlessly bridging...</p>
  <div class="round" style="left:168px;top:568px;background:#c99896;border:1px solid #fff">
    <svg width="12" height="10" viewBox="0 0 12 10"><path d="M1 5h10M7 1l4 4-4 4" stroke="#fff" stroke-width="1.2" fill="none"/></svg>
  </div>
</div>

<!-- ways -->
<div class="photo" role="img" aria-label="Dark photo of business people shaking hands" style="left:0;top:2418px;width:1200px;height:407px;background:linear-gradient(90deg,#3a3a3c 0%,#4d4d4f 50%,#38383a 100%)"></div>
<h2 class="display abs" style="left:0;width:1200px;text-align:center;top:2481px;font-size:36px;color:#fff">Ways we can work together</h2>
<div class="abs" style="left:465px;top:2560px;width:1px;height:120px;background:rgba(255,255,255,.25)"></div>
<svg class="abs" style="left:305px;top:2562px" width="56" height="62" viewBox="0 0 56 62" fill="none" stroke="#c98886" stroke-width="2">
  <circle cx="28" cy="18" r="11"/><path d="M14 18a14 14 0 0 1 28 0"/><rect x="10" y="17" width="5" height="9"/><rect x="41" y="17" width="5" height="9"/>
  <path d="M8 60V46a10 10 0 0 1 10-10h20a10 10 0 0 1 10 10v14z"/><rect x="18" y="42" width="20" height="13"/>
</svg>
<svg class="abs" style="left:570px;top:2560px" width="60" height="64" viewBox="0 0 60 64" fill="none" stroke="#c98886" stroke-width="2">
  <rect x="4" y="6" width="38" height="50" rx="2"/><rect x="15" y="2" width="16" height="7"/>
  <path d="M10 20l3 3 5-5M22 21h14M10 32l3 3 5-5M22 33h10M10 44h6M22 45h6"/>
  <circle cx="46" cy="48" r="12"/><path d="M40 44h3l2 7h7l2-5h-10"/>
</svg>
<svg class="abs" style="left:832px;top:2560px" width="68" height="64" viewBox="0 0 68 64" fill="none" stroke="#c98886" stroke-width="2">
  <circle cx="34" cy="32" r="28"/><path d="M60 20a28 28 0 0 1 2 12"/>
  <rect x="20" y="20" width="28" height="24" rx="2"/><path d="M20 28h28M26 16v6M42 16v6M28 36l4 3 7-6"/>
</svg>
<div class="abs" style="left:233px;width:200px;text-align:center;top:2652px;font-size:16px;color:#fff">1:1 Person Support</div>
<div class="abs" style="left:499px;width:200px;text-align:center;top:2652px;font-size:16px;color:#fff">Additional Support</div>
<div class="abs" style="left:766px;width:200px;text-align:center;top:2652px;font-size:16px;color:#fff">Monthly Membership</div>
<div class="btn btn-light" style="left:513px;top:2719px;width:172px;height:36px">Consultation Now!</div>

<!-- testimonials -->
<h2 class="display section-heading abs" style="left:0;width:1200px;text-align:center;top:2889px;font-size:36px">Testimonials</h2>
<div class="quote-card" style="left:148px;top:2974px">
  <div class="quote-mark"><svg width="30" height="20" viewBox="0 0 30 20" fill="none" stroke="#b07674" stroke-width="2"><path d="M12 2C5 4 2 8 2 13a4 4 0 1 0 4-4M28 2c-7 2-10 6-10 11a4 4 0 1 0 4-4"/></svg></div>
  <p class="quote-text">"When we first met Maren, our 12 month old was stuck in a pattern of inconsistent naps and waking every couple of hours through the night. My husband and I were completely exhausted and desperately overwhelmed. Thanks to Maren's flexible approach, evidence-based advice, generous support and gentle methods, we have developed the confidence and skills to make the changes needed to get the sleep we all need and are SO much happier for it!"</p>
</div>
<div class="quote-card" style="left:610px;top:2974px">
  <div class="quote-mark"><svg width="30" height="20" viewBox="0 0 30 20" fill="none" stroke="#b07674" stroke-width="2"><path d="M12 2C5 4 2 8 2 13a4 4 0 1 0 4-4M28 2c-7 2-10 6-10 11a4 4 0 1 0 4-4"/></svg></div>
  <p class="quote-text">"When we first met Maren, our 12 month old was stuck in a pattern of inconsistent naps and waking every couple of hours through the night. My husband and I were completely exhausted and desperately overwhelmed. Thanks to Maren's flexible approach, evidence-based advice, generous support and gentle methods, we have developed the confidence and skills to make the changes needed to get the sleep we all need and are SO much happier for it!"</p>
</div>

<!-- get started -->
<div class="abs" style="left:0;top:3268px;width:1200px;height:500px;background:linear-gradient(180deg,#f3f5f7,#eef1f4)"></div>
<h2 class="display abs" style="left:0;width:1200px;text-align:center;top:3330px;font-size:36px;line-height:44px;color:var(--ink)">Get started with<br><span style="color:var(--rose)">Quillmarsh</span>, today.</h2>
<div class="field" style="left:212px;top:3440px;width:376px;height:35px">Full Name</div>
<div class="field" style="left:610px;top:3440px;width:378px;height:35px">Email Address</div>
<div class="field" style="left:212px;top:3491px;width:376px;height:35px">Phone Number</div>
<div class="field" style="left:610px;top:3491px;width:378px;height:35px">Subject</div>
<div class="field" style="left:212px;top:3542px;width:776px;height:105px">Message...</div>
<div class="btn btn-dark" style="left:513px;top:3663px;width:172px;height:35px">Book a Consultation</div>

<!-- footer -->
<footer class="site-footer">
  <div class="brand" style="left:148px;top:63px;color:#fff">Quillmarsh</div>
  <div class="abs" style="left:148px;top:118px;font-size:13px;color:#fff;text-transform:uppercase">Follow Us:</div>
  <div class="social" style="left:148px;top:148px"></div>
  <div class="social" style="left:194px;top:148px"></div>
  <div class="social" style="left:241px;top:148px"></div>
  <div class="social" style="left:287px;top:148px"></div>

  <div class="footer-head" style="left:542px;top:72px">Quick Links</div>
  <div class="footer-link" style="left:542px;top:109px">Home</div>
  <div class="footer-link" style="left:542px;top:133px">About Us</div>
  <div class="footer-link" style="left:542px;top:158px">Our Services</div>
  <div class="footer-link" style="left:542px;top:182px">Approach</div>
  <div class="footer-link" style="left:542px;top:206px">Contact Us</div>

  <div class="footer-head" style="left:763px;top:72px">Stay in the Loop</div>
  <p class="abs" style="left:763px;top:108px;width:290px;font-size:12.5px;line-height:21px;color:#fff">Sign up with your email address to receive news and updates.</p>
  <div class="abs" style="left:763px;top:162px;font-size:9.5px;font-weight:700;color:#fff;text-transform:uppercase">I am interested in :*</div>
  <div class="radio" style="left:763px;top:183px"><i class="on"></i>Buying a Business</div>
  <div class="radio" style="left:895px;top:183px"><i></i>Selling My Business</div>
  <div class="radio" style="left:763px;top:204px"><i></i>All</div>
  <div class="abs" style="left:763px;top:231px;width:289px;height:34px;border:1px solid #fff;display:flex">
    <div style="flex:1;font-size:12px;color:#fff;padding:9px 12px">Enter Email...</div>
    <div style="width:36px;border-left:1px solid #fff;display:flex;align-items:center;justify-content:center">
      <svg width="12" height="10" viewBox="0 0 12 10"><path d="M1 5h10M7 1l4 4-4 4" stroke="#fff" stroke-width="1.2" fill="none"/></svg>
    </div>
  </div>
  <div class="abs" style="left:148px;top:301px;width:904px;height:1px;background:rgba(255,255,255,.5)"></div>
  <div class="abs" style="left:148px;top:312px;font-size:10.5px;color:#fff">© 2023 <u>Quillmarsh</u>. All Right Reserved.</div>
  <svg class="abs" style="left:1043px;top:313px" width="8" height="12" viewBox="0 0 8 12"><path d="M4 11V1M1 4l3-3 3 3" stroke="#fff" fill="none"/></svg>
</footer>

</body>
</html>
```